Business Card Design

Target Market(s)

ORVAN is a huge indoor horse sports centre, so horse folks, equestrian, rodeo, western performance, breeds etc.....

Industry/Entity Type

Business

Contact Information for Business Card

O.R.V.A.N.
CHAPLAIN
Colin Marsday
colin@pwqvanlow.org
02 58314729 / 0438271605
Weddings, funerals,
general welfare, referrals,
personal development

Requirements
Nice to have
• something horsey on there but not cheesy!

```html
<!DOCTYPE html>
<html lang="en">
<head>
<meta charset="utf-8">
<title>Colin Marsday – O.R.V.A.N. Chaplain</title>
<link rel="stylesheet" href="https://fonts.googleapis.com/css2?family=Arimo:wght@700&family=Noto+Sans:ital,wght@0,400;1,400&display=swap">
<style>
  :root {
    --navy: #15125e;
    --gold: #f6c21e;
    --ink: #000000;
    --slate: #3a3a48;
    --paper: #ffffff;
    --lavender: #cfcfe4;
  }
  html, body {
    margin: 0;
    padding: 0;
    overflow: hidden;
    background: var(--paper);
  }
  .card {
    position: relative;
    width: 1200px;
    height: 741px;
    overflow: hidden;
    background: linear-gradient(to bottom, var(--paper) 0%, var(--paper) 55%, var(--lavender) 100%);
    font-family: "Noto Sans", sans-serif;
  }
  .brand {
    position: absolute;
    left: 112px;
    top: 96px;
    display: flex;
    align-items: center;
    gap: 16px;
  }
  .brand-square {
    width: 44px;
    height: 44px;
    background: var(--gold);
  }
  .brand-text {
    font-family: "Arimo", sans-serif;
    font-weight: 700;
    color: var(--navy);
    line-height: 1.1;
  }
  .brand-name {
    display: block;
    font-size: 46px;
    letter-spacing: 2px;
  }
  .brand-full {
    display: block;
    font-size: 15px;
    margin-top: 4px;
  }
  .identity {
    position: absolute;
    left: 0;
    width: 1288px;
    top: 290px;
    text-align: center;
    font-family: "Arimo", sans-serif;
    font-weight: 700;
  }
  .person-name {
    margin: 0;
    font-size: 66px;
    line-height: 1;
    color: var(--ink);
  }
  .person-role {
    margin: 14px 0 0;
    font-size: 44px;
    line-height: 1;
    color: var(--navy);
    letter-spacing: 1px;
  }
  .contact {
    position: absolute;
    top: 528px;
    font-size: 35px;
    line-height: 42px;
    color: var(--slate);
  }
  .contact-phone { left: 112px; }
  .contact-email { right: 116px; top: 570px; text-align: right; }
  .contact-label { display: block; font-style: normal; }
  .contact-value { display: block; font-style: italic; }
</style>
</head>
<body>
<main class="card">
  <div class="brand">
    <span class="brand-square" aria-hidden="true"></span>
    <span class="brand-text">
      <span class="brand-name">ORVAN</span>
      <span class="brand-full">Orvan Rural Venue and Arena Network</span>
    </span>
  </div>

  <header class="identity">
    <h1 class="person-name">Colin Marsday</h1>
    <p class="person-role">O.R.V.A.N. CHAPLAIN</p>
  </header>

  <div class="contact contact-phone">
    <span class="contact-label">Phone</span>
    <span class="contact-value">02 58314729</span>
    <span class="contact-value">04 38271605</span>
  </div>

  <div class="contact contact-email">
    <span class="contact-label">E-mail</span>
    <span class="contact-value">colin@pwqvanlow.org</span>
  </div>
</main>
</body>
</html>
```